Bramblewick Dill Pickles needs your smart gourmet Design

Looking for a smart design for a dill pickle jar container. The text
Bramblewick Dill Pickles.
Simply Picklelicious.

A tasty reason to raid the refrigerator.

Target Market(s)

Foodies, farmers market types.

Font styles to use
Serif
Sans Serif

Colors

Designer to choose colors to be used in the design.

Requirements
Must have
• Attractive design to entice foodies to buy my Pickles. Not cluttered, easy to read.
Nice to have
• Pickles, garlic. Modern.
Should not have
• Clutter. No script text.

```html
<!DOCTYPE html>
<html lang="en">
<head>
<meta charset="utf-8">
<title>Bramblewick Dill Pickles – Jar Labels</title>
<link rel="stylesheet" href="https://fonts.googleapis.com/css2?family=Open+Sans:wght@400&family=Oswald:wght@500;600&display=swap">
<style>
  :root {
    --backdrop: #ece9e1;
    --slate-frame: #9b9b9b;
    --slate-ink: #a4a4a4;
    --slate-ground: #232323;
    --herb-frame: #a5b43e;
    --herb-ink: #a9b843;
    --herb-ground: #1d2116;
    --garlic-light: #f3ece6;
    --garlic-shade: #d9c3c4;
  }
  html, body {
    margin: 0;
    padding: 0;
    width: 1200px;
    height: 821px;
    overflow: hidden;
    background: var(--backdrop);
  }
  .canvas {
    position: relative;
    width: 1200px;
    height: 821px;
  }
  .label {
    position: absolute;
    display: block;
  }
  .label--slate { left: 130px; top: 127px; width: 400px; height: 567px; }
  .label--herb  { left: 655px; top: 118px; width: 427px; height: 584px; }
  .label__variety { font-family: "Open Sans", sans-serif; font-weight: 400; }
  .label__product { font-family: "Oswald", sans-serif; font-weight: 600; }
  .label__slogan  { font-family: "Open Sans", sans-serif; font-weight: 400; }
  .label__tagline { font-family: "Oswald", sans-serif; font-weight: 500; }
</style>
</head>
<body>
<main class="canvas">

  <!-- Slate edition -->
  <svg class="label label--slate" viewBox="0 0 510 723" xmlns="http://www.w3.org/2000/svg">
    <defs>
      <polygon id="star" points="0,-13 3.8,-4 13,-4 5.6,1.6 8.2,11 0,5.4 -8.2,11 -5.6,1.6 -13,-4 -3.8,-4"/>
      <linearGradient id="garlicSlate" x1="0" y1="0" x2="0" y2="1">
        <stop offset="0" stop-color="var(--garlic-light)"/>
        <stop offset="1" stop-color="var(--garlic-shade)"/>
      </linearGradient>
    </defs>
    <path class="label__frame" d="M0,100 Q0,84 15,78 L255,0 L495,78 Q510,84 510,100 L510,723 L0,723 Z" fill="var(--slate-frame)"/>
    <path class="label__ground" d="M10,104 Q10,90 23,85 L255,10 L487,85 Q500,90 500,104 L500,713 L10,713 Z" fill="var(--slate-ground)"/>
    <path class="label__keyline" d="M26,112 Q26,100 37,96 L255,26 L473,96 Q484,100 484,112 L484,697 L26,697 Z" fill="none" stroke="var(--slate-frame)" stroke-width="3"/>

    <g fill="var(--slate-ink)">
      <use href="#star" x="112" y="160"/><use href="#star" x="148" y="160"/>
      <use href="#star" x="370" y="160"/><use href="#star" x="406" y="160"/>
    </g>
    <rect role="img" aria-label="Illustration of garlic bulbs and cloves" x="190" y="100" width="128" height="86" rx="40" fill="url(#garlicSlate)"/>

    <text class="label__variety" x="267" y="258" font-size="40" text-anchor="middle" fill="var(--slate-ink)" textLength="300" lengthAdjust="spacingAndGlyphs">BRAMBLEWICK</text>
    <line x1="38" y1="283" x2="475" y2="283" stroke="var(--slate-frame)" stroke-width="3"/>
    <text class="label__product" x="260" y="460" font-size="205" text-anchor="middle" fill="var(--slate-ink)" textLength="282" lengthAdjust="spacingAndGlyphs">DILL</text>
    <text class="label__product" x="255" y="582" font-size="148" text-anchor="middle" fill="var(--slate-ink)" textLength="380" lengthAdjust="spacingAndGlyphs">PICKLES</text>
    <line x1="38" y1="606" x2="475" y2="606" stroke="var(--slate-frame)" stroke-width="3"/>
    <text class="label__slogan" x="260" y="653" font-size="33" text-anchor="middle" fill="var(--slate-ink)" textLength="364" lengthAdjust="spacingAndGlyphs">SIMPLY PICKLELICIOUS</text>
    <text class="label__tagline" x="257" y="684" font-size="15" text-anchor="middle" fill="var(--slate-ink)" textLength="252" lengthAdjust="spacingAndGlyphs">A TASTY REASON TO RAID THE REFRIGERATOR</text>
  </svg>

  <!-- Herb edition -->
  <svg class="label label--herb" viewBox="0 0 545 745" xmlns="http://www.w3.org/2000/svg">
    <defs>
      <polygon id="starHerb" points="0,-13 3.8,-4 13,-4 5.6,1.6 8.2,11 0,5.4 -8.2,11 -5.6,1.6 -13,-4 -3.8,-4"/>
      <linearGradient id="garlicHerb" x1="0" y1="0" x2="0" y2="1">
        <stop offset="0" stop-color="var(--garlic-light)"/>
        <stop offset="1" stop-color="var(--garlic-shade)"/>
      </linearGradient>
    </defs>
    <path class="label__frame" d="M0,24 Q0,2 22,2 L62,2 L272,70 L483,2 L523,2 Q545,2 545,24 L545,745 L0,745 Z" fill="var(--herb-frame)"/>
    <path class="label__ground" d="M12,26 Q12,14 24,14 L60,14 L272,83 L485,14 L521,14 Q533,14 533,26 L533,733 L12,733 Z" fill="var(--herb-ground)"/>
    <path class="label__keyline" d="M26,733 L26,30 L62,30 L272,98 L483,30 L519,30 L519,733" fill="none" stroke="var(--herb-frame)" stroke-width="5"/>
    <path class="label__keyline" d="M42,733 L42,46 L64,46 L272,113 L481,46 L503,46 L503,733" fill="none" stroke="var(--herb-frame)" stroke-width="5"/>
    <path class="label__keyline" d="M57,733 L57,62 L66,62 L272,128 L479,62 L488,62 L488,733" fill="none" stroke="var(--herb-frame)" stroke-width="5"/>

    <g fill="var(--herb-ink)">
      <use href="#starHerb" x="118" y="152"/><use href="#starHerb" x="152" y="152"/>
      <use href="#starHerb" x="393" y="152"/><use href="#starHerb" x="427" y="152"/>
    </g>
    <rect role="img" aria-label="Illustration of garlic bulbs and cloves" x="226" y="140" width="92" height="58" rx="26" fill="url(#garlicHerb)"/>

    <text class="label__variety" x="282" y="254" font-size="42" text-anchor="middle" fill="var(--herb-ink)" textLength="296" lengthAdjust="spacingAndGlyphs">BRAMBLEWICK</text>
    <line x1="57" y1="280" x2="488" y2="280" stroke="var(--herb-frame)" stroke-width="4"/>
    <text class="label__product" x="273" y="466" font-size="212" text-anchor="middle" fill="var(--herb-ink)" textLength="297" lengthAdjust="spacingAndGlyphs">DILL</text>
    <text class="label__product" x="271" y="603" font-size="160" text-anchor="middle" fill="var(--herb-ink)" textLength="402" lengthAdjust="spacingAndGlyphs">PICKLES</text>
    <line x1="57" y1="627" x2="488" y2="627" stroke="var(--herb-frame)" stroke-width="4"/>
    <text class="label__slogan" x="277" y="674" font-size="35" text-anchor="middle" fill="var(--herb-ink)" textLength="388" lengthAdjust="spacingAndGlyphs">SIMPLY PICKLELICIOUS</text>
    <text class="label__tagline" x="274" y="706" font-size="17" text-anchor="middle" fill="var(--herb-ink)" textLength="268" lengthAdjust="spacingAndGlyphs">A TASTY REASON TO RAID THE REFRIGERATOR</text>
  </svg>

</main>
</body>
</html>
```